Email Signature

We want a new email signature designed that will include an employees picture and our logo at minimum. Of course contact info as well.

For the sample please create the new signature for Dale Prewitt...extra pics provided
please visit our website www.BrightwayUpkeep.com

Need to limit links to our website....government email servers strip out many.
Updates

I have a new draft design I'd like to work from...simple and clean.Needs:LogoDisclaimerand a bit of colorI'd like to make selection this week. Added Tuesday, October 24, 2017

Target Market(s)

other professional businesses

Requirements
Must have
• picture & Logo
• new look and something that auto scales to the emails window.
• Would like to have a new tag line "

```html
<!DOCTYPE html>
<html lang="en">
<head>
<meta charset="utf-8">
<title>Email Signature – Dale Prewitt</title>
<link href="https://fonts.googleapis.com/css2?family=Oswald:wght@500;600&display=swap" rel="stylesheet">
<style>
  :root {
    --paper: #ffffff;
    --charcoal: #262626;
    --signal-red: #ee1530;
    --rose-red: #f21a4f;
    --flame-orange: #ff5a1f;
    --ink-light: #ffffff;
    --photo-light: #e9e6e3;
    --photo-dark: #3a3b40;
  }
  html, body {
    margin: 0;
    padding: 0;
    overflow: hidden;
    background: var(--paper);
  }
  .signature {
    position: relative;
    width: 1200px;
    height: 400px;
    overflow: hidden;
    background: var(--paper);
    font-family: "Oswald", "Arial Narrow", sans-serif;
    text-transform: uppercase;
    color: var(--ink-light);
  }
  .shapes {
    position: absolute;
    inset: 0;
    width: 1200px;
    height: 400px;
  }
  .portrait {
    position: absolute;
    left: 200px;
    top: 0;
    width: 287px;
    height: 400px;
    background: linear-gradient(180deg, var(--photo-light) 0%, #cbbdb4 35%, var(--photo-dark) 75%, #1f2024 100%);
  }
  .greeting {
    position: absolute;
    left: 19px;
    top: 240px;
    font-weight: 500;
    font-size: 22px;
    line-height: 35px;
    letter-spacing: 0.3px;
  }
  .person {
    position: absolute;
    left: 175px;
    top: 320px;
    width: 330px;
    text-align: center;
    font-weight: 500;
    font-size: 21px;
    line-height: 29px;
    letter-spacing: 0.3px;
  }
  .company {
    position: absolute;
    left: 720px;
    top: 126px;
    width: 300px;
    text-align: center;
    color: var(--signal-red);
    font-weight: 600;
    font-size: 30px;
    line-height: 34px;
    letter-spacing: 0.5px;
  }
  .company-sub {
    display: block;
    font-size: 15px;
    line-height: 20px;
    letter-spacing: 2px;
  }
  .contact {
    position: absolute;
    left: 600px;
    top: 262px;
    width: 700px;
    margin: 0;
    text-align: center;
    font-weight: 500;
    font-size: 14px;
    line-height: 22.5px;
    letter-spacing: 0.2px;
  }
  .contact span { display: block; }
</style>
</head>
<body>
<main class="signature">
  <div class="portrait" role="img" aria-label="Portrait photo of Dale Prewitt in a dark suit and red tie"></div>

  <svg class="shapes" viewBox="0 0 900 300" aria-hidden="true">
    <polygon points="398,0 448,0 380,236 330,236" fill="var(--flame-orange)"/>
    <polygon points="440,0 475,0 362,300 318,300" fill="var(--signal-red)"/>
    <polygon points="470,0 900,0 900,300 355,300" fill="var(--charcoal)"/>
    <polygon points="890,98 900,98 900,185 862,185" fill="var(--flame-orange)"/>
    <polygon points="893,170 900,170 900,250 868,250" fill="var(--signal-red)"/>
    <polygon points="0,168 145,168 112,300 0,300" fill="var(--signal-red)"/>
    <polygon points="138,238 362,238 345,300 120,300" fill="var(--rose-red)"/>
  </svg>

  <p class="greeting">Thanks &amp;<br>Regards<br>From</p>

  <p class="person">Dale Prewitt<br>Vice President</p>

  <p class="company">Brightway Upkeep<span class="company-sub">Incorporated</span></p>

  <address class="contact">
    <span>415 Harbor Avenue Suite B</span>
    <span>Dunmore Maryland 21000</span>
    <span>Phone 877-555-0142 * Fax: 877-555-0143</span>
    <span>Electrical * Roadway * Commercial * Sports Lighting * Traffic Signals</span>
    <span>Ashford Virginia * Kellam Virginia * Dunmore Maryland * Westbrook Maryland</span>
  </address>
</main>
</body>
</html>
```